Rex Tollbridge (Burn The Stack) CD Cover Design

Professional Cd cover design needed. No photo of the artist necessary for this cover. You can search Rex Tollbridge on YouTube for a feel of the artist, inspiration, etc. Song (Burn The Stack)!

Target Market(s)

Big money makers , Hustlers, those who don't mind spending cash.

Colors

Designer to choose colors to be used in the design.

Requirements
Nice to have
• Any symbols related to money.

```html
<!DOCTYPE html>
<html lang="en">
<head>
<meta charset="utf-8">
<title>Rex Tollbridge – Burn The Stack</title>
<link rel="stylesheet" href="https://fonts.googleapis.com/css2?family=Yellowtail&family=Special+Elite&family=Playfair+Display:wght@900&display=swap">
<style>
  :root {
    --bg: #000000;
    --red: #ff0000;
    --red-deep: #c80000;
    --title: #ffffff;
    --artist: #c9c9c9;
  }
  html, body {
    margin: 0;
    padding: 0;
    overflow: hidden;
    background: var(--bg);
  }
  .cover {
    position: relative;
    width: 1200px;
    height: 1200px;
    background: var(--bg);
    overflow: hidden;
  }
  .brush-streaks {
    position: absolute;
    left: 0;
    top: 0;
    width: 1200px;
    height: 1200px;
  }
  .dollar-mark {
    position: absolute;
    left: 745px;
    top: 300px;
    font-family: "Playfair Display", serif;
    font-weight: 900;
    font-size: 500px;
    line-height: 1;
    color: var(--red);
    margin: 0;
  }
  .song-title {
    position: absolute;
    left: 170px;
    top: 330px;
    width: 640px;
    margin: 0;
    font-family: "Yellowtail", cursive;
    font-weight: 400;
    color: var(--title);
    font-size: 200px;
    line-height: 0.98;
    text-align: center;
    transform: rotate(-4deg);
  }
  .song-title .line {
    display: block;
  }
  .song-title .line-two {
    font-size: 170px;
  }
  .artist-name {
    position: absolute;
    right: 60px;
    top: 1010px;
    margin: 0;
    font-family: "Special Elite", monospace;
    font-size: 66px;
    letter-spacing: 2px;
    color: var(--artist);
    text-transform: uppercase;
  }
</style>
</head>
<body>
  <main class="cover">
    <svg class="brush-streaks" viewBox="0 0 1200 1200" role="img" aria-label="Red diagonal brush-stroke streaks behind the title">
      <defs>
        <linearGradient id="streak-fill" x1="0" y1="0" x2="1" y2="1">
          <stop offset="0" stop-color="var(--red)" style="stop-color:#ff0000"/>
          <stop offset="1" stop-color="var(--red-deep)" style="stop-color:#d00000"/>
        </linearGradient>
      </defs>
      <polygon points="330,30 800,40 720,520 560,980 70,1000 140,560" fill="url(#streak-fill)"/>
    </svg>

    <p class="dollar-mark" aria-hidden="true">$</p>

    <h1 class="song-title">
      <span class="line line-one">Burn</span>
      <span class="line line-two">the Stack</span>
    </h1>

    <p class="artist-name">Rex Tollbridge</p>
  </main>
</body>
</html>
```